Each Lady Ought to Learn Her R.I.M.shape

We need a book cover design for a book that will be used as a confidence coaching tool for women of all races, and walks of life . The title is a play on words because CUP is an acronym that stands for calling, uniqueness, and her purpose. The twist of the book is that this is from a male perspective.
The book will focus on Knowing the Bra types available and how bras represent the different kind of people you need in your life.
Updates

There are certain dynamics requested for this book cover i.e., tape measure, bra etc.  Please view pictures attached to file. i would like to see a book cover with breast covered maybe with hands. 

Target Market(s)

every female in the population of the world from every walk of life from 12-99

Requirements
Must have
• The book cover will also be used for the product line i.e. follow up work book and teaching tools. Measuring tapes, bras and breast are the main theme. Not too explicit that it wont be allowed on the shelves at Pellman and Crowe but I do want it to push the envelope TO THE POINT IT MAKES YOU WANT TO PICK IT UP!
Nice to have
• a woman measuring her breast or bust line .......also bra sizes like 36c 44dd 38b ect.
Should not have
• no naked women or faces of women or below the navel or above the neck pictures if breast revealed they must be covered by hands or bra or flowers ect.

```html
<!DOCTYPE html>
<html lang="en">
<head>
<meta charset="utf-8">
<title>Each Lady Ought to Learn Her R.I.M.shape — Book Cover</title>
<link href="https://fonts.googleapis.com/css2?family=Quicksand:wght@300;500;600;700&family=Alex+Brush&display=swap" rel="stylesheet">
<style>
  :root {
    --page-bg: #f8e1eb;
    --ocean-deep: #1677ad;
    --ocean-mid: #1c8fc4;
    --ocean-light: #2a9fd0;
    --ocean-band: #3aa8d6;
    --rose: #e0577e;
    --blush: #f4c7df;
    --bikini-pink: #f6dde6;
    --white: #ffffff;
    --line-cream: #f4ecd0;
  }
  * { margin: 0; padding: 0; box-sizing: border-box; }
  html, body {
    width: 1200px;
    height: 816px;
    overflow: hidden;
    background: var(--page-bg);
  }
  .book-cover {
    position: absolute;
    left: 320px;
    top: 45px;
    width: 560px;
    height: 726px;
    overflow: hidden;
    background:
      linear-gradient(180deg,
        var(--ocean-mid) 0%,
        var(--ocean-light) 22%,
        var(--ocean-deep) 30%,
        var(--ocean-mid) 45%,
        var(--ocean-band) 55%,
        var(--ocean-mid) 68%,
        var(--ocean-light) 85%,
        var(--ocean-mid) 100%);
    font-family: 'Quicksand', sans-serif;
    color: var(--white);
  }
  .clothesline {
    position: absolute;
    inset: 0;
  }
  .bikini-photo {
    position: absolute;
    left: 204px;
    top: 207px;
    width: 320px;
    height: 485px;
    border-radius: 40% 40% 30% 30% / 18% 18% 50% 50%;
    background: radial-gradient(ellipse at 50% 28%, var(--bikini-pink) 0%, rgba(246,221,230,0.55) 35%, rgba(246,221,230,0) 70%);
  }
  .title-line {
    position: absolute;
    white-space: nowrap;
    line-height: 1;
  }
  .title-each   { left: 47px; top: 43px; font-size: 44px; font-weight: 600; }
  .title-lady   {
    left: 69px; top: 80px;
    font-family: 'Alex Brush', cursive;
    font-size: 100px;
    color: var(--rose);
    -webkit-text-stroke: 4px var(--white);
    paint-order: stroke fill;
  }
  .title-ought  { left: 36px; top: 224px; font-size: 37px; font-weight: 700; }
  .title-learn  { left: 36px; top: 267px; font-size: 37px; font-weight: 700; }
  .title-rim    { left: 36px; top: 318px; font-size: 56px; font-weight: 500; color: var(--blush); letter-spacing: 1px; }
  .title-shape  { left: 38px; top: 384px; font-size: 22px; font-weight: 300; text-transform: uppercase; }
  .size-samples {
    position: absolute;
    left: 232px;
    top: 465px;
    font-size: 32px;
    font-weight: 600;
    white-space: nowrap;
  }
  .author-label {
    position: absolute;
    left: 33px;
    top: 629px;
    font-size: 14px;
    font-weight: 300;
    text-transform: uppercase;
  }
  .author-bar {
    position: absolute;
    left: 0;
    top: 651px;
    width: 141px;
    height: 22px;
    background: var(--white);
  }
  .accent-bar {
    position: absolute;
    left: 0;
    top: 676px;
    width: 216px;
    height: 22px;
    background: var(--rose);
  }
</style>
</head>
<body>
  <main class="book-cover">
    <div class="bikini-photo" role="img" aria-label="Photo of a pale pink string bikini top pinned to a clothesline with wooden pegs"></div>
    <svg class="clothesline" width="560" height="726" viewBox="0 0 560 726" aria-hidden="true">
      <path d="M0 161 Q280 205 560 226" fill="none" stroke="var(--line-cream)" stroke-width="2.5"/>
    </svg>

    <h1 class="book-title">
      <span class="title-line title-each">Each</span>
      <span class="title-line title-lady">Lady</span>
      <span class="title-line title-ought">Ought to</span>
      <span class="title-line title-learn">Learn Her</span>
      <span class="title-line title-rim">R.I.M.</span>
      <span class="title-line title-shape">shape</span>
    </h1>

    <p class="size-samples">36c 44dd 38b</p>

    <p class="author-label">Your Name</p>
    <div class="author-bar"></div>
    <div class="accent-bar"></div>
  </main>
</body>
</html>
```